Business Cards for Internet Security Company

Awesome designers! This is the opportunity to help design cards for a forward thinking network security company. They use threat information gathered from peer groups to make intelligent decisions on what threats are relevant and which arent. ( not that you need this to do designs, but just so you know where they are coming from. ) :-)

We'd like to see a two side design and the deliverables will be in illustrator 4. The logo is attached and the logo colors are attached in the JPG and I've attached a an eps of the logo and icon

Security

```html
<!DOCTYPE html>
<html lang="en">
<head>
<meta charset="utf-8">
<title>Kelvane Business Cards</title>
<link rel="stylesheet" href="https://fonts.googleapis.com/css2?family=Source+Sans+3:ital,wght@0,400;0,600;1,400&display=swap">
<style>
  :root {
    --backdrop: #e6e8ec;
    --card: #2f2e30;
    --brand-blue: #4a8fc4;
    --rule: #4e6f8c;
    --shadow: rgba(0, 0, 0, 0.28);
  }
  * { margin: 0; padding: 0; box-sizing: border-box; }
  html, body {
    width: 1200px;
    height: 1195px;
    overflow: hidden;
    background: var(--backdrop);
    font-family: "Source Sans 3", "Myriad Pro", sans-serif;
  }
  .sheet {
    width: 1200px;
    height: 1195px;
    display: flex;
    flex-direction: column;
    align-items: center;
    justify-content: center;
    gap: 34px;
  }
  .card {
    position: relative;
    width: 960px;
    height: 549px;
    background: var(--card);
    border-radius: 4px;
    box-shadow: 0 10px 28px var(--shadow);
    color: var(--brand-blue);
    overflow: hidden;
  }
  .brand {
    display: flex;
    align-items: center;
    color: var(--brand-blue);
    font-weight: 600;
    letter-spacing: 0.01em;
  }
  .brand-dot {
    border-radius: 50%;
    background: var(--brand-blue);
    flex: none;
  }
  /* front */
  .card-front {
    display: flex;
    align-items: center;
    justify-content: center;
  }
  .card-front .brand { font-size: 170px; gap: 36px; }
  .card-front .brand-dot { width: 120px; height: 120px; }
  /* back */
  .card-back .brand {
    position: absolute;
    left: 70px;
    top: 62px;
    font-size: 96px;
    gap: 22px;
  }
  .card-back .brand-dot { width: 66px; height: 66px; }
  .person {
    position: absolute;
    left: 70px;
    top: 250px;
  }
  .person-name { font-size: 38px; font-weight: 600; line-height: 1.1; }
  .person-title { font-size: 33px; font-style: italic; line-height: 1.2; }
  .address {
    position: absolute;
    left: 70px;
    top: 372px;
    font-size: 27px;
    line-height: 1.22;
  }
  .contact-line {
    display: flex;
    align-items: center;
    gap: 12px;
  }
  .contact-line svg { width: 24px; height: 24px; flex: none; }
  .direct {
    position: absolute;
    right: 70px;
    top: 258px;
    font-size: 27px;
    line-height: 1.45;
  }
  .direct .contact-line svg { width: 30px; height: 26px; }
  .card-rule {
    position: absolute;
    left: 70px;
    right: 70px;
    bottom: 42px;
    height: 1px;
    background: var(--rule);
  }
</style>
</head>
<body>
<main class="sheet">
  <section class="card card-front" aria-label="Card front">
    <div class="brand"><span class="brand-dot"></span><span class="brand-name">Kelvane</span></div>
  </section>

  <section class="card card-back" aria-label="Card back">
    <div class="brand"><span class="brand-dot"></span><span class="brand-name">Kelvane</span></div>

    <div class="person">
      <p class="person-name">Mara Tolliver</p>
      <p class="person-title">Chief Executive Officer &amp; Co-Founder</p>
    </div>

    <address class="address" style="font-style:normal">
      <p>418 Harbor Point Dr St.</p>
      <p>Fairmont, OH 45012</p>
      <p class="contact-line">
        <svg viewBox="0 0 24 24" aria-hidden="true"><rect x="6" y="2" width="12" height="20" rx="2.5" fill="var(--brand-blue)"/><rect x="8.5" y="5" width="7" height="8" fill="var(--card)"/><circle cx="12" cy="18" r="1.4" fill="var(--card)"/></svg>
        <span>555-014-2287</span>
      </p>
    </address>

    <div class="direct">
      <p class="contact-line">
        <svg viewBox="0 0 30 26" aria-hidden="true"><rect x="8" y="2" width="14" height="7" fill="none" stroke="var(--brand-blue)" stroke-width="2"/><rect x="2" y="9" width="26" height="10" rx="2" fill="var(--brand-blue)"/><rect x="8" y="15" width="14" height="9" fill="var(--card)" stroke="var(--brand-blue)" stroke-width="2"/></svg>
        <span>555-019-6630</span>
      </p>
      <p class="contact-line">
        <svg viewBox="0 0 30 26" aria-hidden="true"><rect x="2" y="4" width="26" height="18" fill="none" stroke="var(--brand-blue)" stroke-width="2"/><path d="M2 4 L15 15 L28 4" fill="none" stroke="var(--brand-blue)" stroke-width="2"/></svg>
        <span>m.tolliver@kelvane.com</span>
      </p>
    </div>

    <div class="card-rule"></div>
  </section>
</main>
</body>
</html>
```